Harborline Property Group - New Agent Opportunity Overview

We want to create a one (1) page brochure to highlight what Harborline Property Group (a real estate brokerage) offers new agents. I have uploaded a Word doc that has all the text we want on the flyer. We want a professional looking design.
Industry/Entity Type
Real Estate Agent
Colors
3176b5
33a6d7

```html
<!DOCTYPE html>
<html lang="en">
<head>
<meta charset="utf-8">
<title>Harborline Property Group – New Agent Opportunity</title>
<link rel="stylesheet" href="https://fonts.googleapis.com/css2?family=Montserrat:wght@400;600;700;800&family=Open+Sans:wght@400;600;700&display=swap">
<style>
  :root{
    --brand-blue:#3176b5;
    --brand-cyan:#33a6d7;
    --sky-panel:#85bde1;
    --heading-blue:#2f6fb3;
    --paper:#f2f3f5;
    --footer-grey:#e8e8e9;
    --ink:#1f2430;
    --white:#ffffff;
  }
  *{margin:0;padding:0;box-sizing:border-box}
  html,body{width:1200px;height:1200px;overflow:hidden;background:#ffffff}
  body{font-family:"Open Sans",Arial,sans-serif;color:var(--ink);position:relative}
  .flyer{position:absolute;left:177px;top:2px;width:846px;height:1196px;background:var(--paper);overflow:hidden}
  .abs{position:absolute}

  .brand-name{left:59px;top:30px;font-family:"Montserrat",Arial,sans-serif;font-weight:700;font-size:17px;letter-spacing:3px;color:var(--ink);display:flex;align-items:center;gap:10px}
  .brand-name .mark{width:14px;height:14px;background:var(--brand-blue)}

  .opening{left:56px;top:118px;font-family:"Montserrat",Arial,sans-serif;font-size:24px;color:var(--brand-blue);white-space:nowrap}
  .opening strong{font-weight:700}

  .hero{left:0;top:167px;width:846px;height:426px}
  .hero-photo{position:absolute;inset:0;background:linear-gradient(90deg,#f3efe6 0%,#dcd3bd 25%,#8fa3b8 42%,#b89583 62%,#8c6b5e 80%,#5a4a44 100%)}
  .headline{position:absolute;left:56px;top:15px;font-family:"Montserrat",Arial,sans-serif;font-weight:800;font-size:99px;line-height:102px;color:var(--white);text-shadow:0 4px 10px rgba(0,0,0,.35);letter-spacing:-1px;white-space:nowrap}
  .headline .accent{color:var(--brand-cyan)}
  .join-banner{position:absolute;left:443px;top:343px;width:403px;height:83px}
  .join-text{position:absolute;left:509px;top:360px;font-family:"Montserrat",Arial,sans-serif;font-weight:700;color:var(--white)}
  .join-text .big{font-size:28px;line-height:32px;display:block}
  .join-text .small{font-size:21px;line-height:26px;display:block;white-space:nowrap}

  .benefits{left:0;top:593px;width:846px;height:460px;background:var(--sky-panel)}
  .divider{position:absolute;left:410px;top:24px;height:404px;border-left:2px dotted var(--white)}
  .col{position:absolute;top:32px}
  .col-left{left:59px}
  .col-right{left:444px}
  .section-title{font-family:"Montserrat",Arial,sans-serif;font-weight:700;font-size:19px;color:var(--heading-blue);line-height:24px;white-space:nowrap}
  .perks{list-style:none;font-size:15.5px;color:var(--white);line-height:21.8px;margin-top:2px}
  .perks li{padding-left:18px;position:relative;white-space:nowrap}
  .perks li::before{content:"o";position:absolute;left:0}
  .perks li.sub{padding-left:45px}
  .perks li.sub::before{left:27px}
  .support{margin-top:88px}

  .split-table{position:absolute;left:59px;top:263px;width:300px}
  .split-head{position:absolute;top:0;font-family:"Montserrat",Arial,sans-serif;color:var(--white);font-size:22px;line-height:24px;width:122px;padding-bottom:6px;border-bottom:3px solid var(--brand-blue)}
  .split-head b{display:block;font-weight:700;color:var(--brand-cyan);font-size:25px}
  .split-row{position:absolute;left:0;width:300px;font-weight:700;font-size:15.5px;line-height:18px}
  .split-row .deal{color:var(--brand-cyan);width:140px;display:inline-block}
  .split-row .share{position:absolute;left:169px;top:0;color:var(--white);white-space:nowrap}

  .footer{left:0;top:1053px;width:846px;height:115px;background:var(--footer-grey)}
  .office{position:absolute;left:59px;top:26px;font-size:13.5px;line-height:20px}
  .office strong{font-family:"Montserrat",Arial,sans-serif;font-weight:700;font-size:14px}
  .contacts{position:absolute;left:265px;top:26px;font-size:13px;line-height:19.5px;list-style:none}
  .contacts li{display:flex;align-items:center;gap:10px}
  .contacts svg{width:14px;height:12px;fill:var(--ink)}
  .call-box{left:442px;top:1053px;width:404px;height:84px}
  .call-text{position:absolute;left:139px;top:14px;color:var(--white)}
  .call-text .number{font-size:22px;line-height:28px;display:block}
  .call-text .cta{font-size:13px}
  .call-icon{position:absolute;left:88px;top:24px;width:40px;height:36px}
</style>
</head>
<body>
<main class="flyer">
  <div class="abs brand-name"><span class="mark"></span>HARBORLINE PROPERTY GROUP</div>

  <p class="abs opening">HPG Home Center Millbrook, Maryland is <strong>Now Open!</strong></p>

  <section class="abs hero">
    <div class="hero-photo" role="img" aria-label="Photo of a hand holding a model house in front of a blurred real estate agent"></div>
    <h1 class="headline">IGNITE <span class="accent">YOUR</span><br>REAL ESTATE<br>BUSINESS</h1>
    <svg class="join-banner" viewBox="0 0 403 83" aria-hidden="true">
      <defs><linearGradient id="joinGrad" x1="0" x2="1"><stop offset="0" stop-color="#4aa7d8"/><stop offset="1" stop-color="#3f95cc"/></linearGradient></defs>
      <polygon points="60,0 403,0 403,83 0,83" fill="url(#joinGrad)"/>
    </svg>
    <div class="join-text"><span class="big">Join</span><span class="small">Harborline Property Group</span></div>
  </section>

  <section class="abs benefits">
    <div class="divider"></div>
    <div class="col col-left">
      <h2 class="section-title">CONSUMER DIRECT ADVANTAGE</h2>
      <ul class="perks">
        <li>Lender Referrals</li>
        <li>Nestfinder Leads</li>
        <li>Shared Lender Leads</li>
        <li>Homeview.com / ListingsNearby.com</li>
        <li>Credit Trigger Campaigns</li>
        <li>Consumer Behavior Campaigns</li>
        <li>HPG Call Center Marketing Team</li>
        <li>HPG Sponsored Local Events</li>
      </ul>
    </div>
    <div class="split-table">
      <div class="split-head" style="left:0">TYPE OF<b>DEAL</b></div>
      <div class="split-head" style="left:165px">COMMISSION<b>SPLIT</b></div>
      <div class="split-row" style="top:76px"><span class="deal">Self-Generated</span><span class="share">90% /10%</span></div>
      <div class="split-row" style="top:107px"><span class="deal">Lender Referred Leads</span><span class="share">70% /30%</span></div>
      <div class="split-row" style="top:151px"><span class="deal">HPG Generated Leads / Referrals</span><span class="share">55% /45%</span></div>
    </div>
    <div class="col col-right">
      <h2 class="section-title">MAXIMIZED COMPENSATION</h2>
      <ul class="perks">
        <li>No desk fees. No royalty fees. No franchise fees.</li>
        <li>Company paid E&amp;O</li>
        <li>Transaction fee of $550 includes<br>Transaction Coordinator</li>
      </ul>
      <h2 class="section-title support">COMPLETE SUPPORT SYSTEM</h2>
      <ul class="perks">
        <li>Powerful Suite of Cloud Based Tools</li>
        <li class="sub">IDX, CRM and Transaction Management</li>
        <li>HPG Call Center Support for Leads and Deals</li>
        <li>Transaction Coordinator</li>
        <li>Virtual Assistants Available</li>
        <li>24/7 Workspace Access</li>
        <li>Coaching / Mentoring</li>
        <li>Social Media / MarketingExpertise</li>
        <li>Nationwide Partnerships with Top Lenders</li>
      </ul>
    </div>
  </section>

  <footer class="abs footer">
    <div class="office"><strong>Harborline Property Group</strong><br>Millbrook<br>MARYLAND</div>
    <ul class="contacts">
      <li><svg viewBox="0 0 14 12"><path d="M1 4C1 1 13 1 13 4L11 5 10 3H4L3 5ZM3 6H11L13 11H1Z"/></svg>000 00000000</li>
      <li><svg viewBox="0 0 14 12"><path d="M0 1H14V11H0ZM1.5 2.5 7 7 12.5 2.5V9.5H1.5Z" fill-rule="evenodd"/></svg>call@harborlinehomes.com</li>
      <li><svg viewBox="0 0 14 12"><path d="M0 0H14V9H8V10.5H10V12H4V10.5H6V9H0ZM1.5 1.5V7.5H12.5V1.5Z" fill-rule="evenodd"/></svg>your site.com</li>
    </ul>
  </footer>
  <div class="abs call-box">
    <svg width="404" height="84" viewBox="0 0 404 84" aria-hidden="true" style="position:absolute;inset:0">
      <polygon points="0,0 404,0 404,84 64,84" fill="var(--brand-blue)"/>
    </svg>
    <svg class="call-icon" viewBox="0 0 40 36" fill="none" stroke="#ffffff" stroke-width="1.5" aria-hidden="true">
      <path d="M2 16 38 2 28 30 18 20Z"/><path d="M38 2 18 20 16 30 22 24"/>
      <path d="M12 24C6 28 6 34 12 34S22 32 26 34" stroke-dasharray="2 2"/>
    </svg>
    <div class="call-text"><span class="number">000 0000 0000</span><span class="cta">Call NOW!</span></div>
  </div>
</main>
</body>
</html>
```